Equine Podcast Cover Art Design

We need catchy cover art for a horse related podcast "Ride Onward Together"
Brief show description"
Whether you want to ride to experience horses, develop yourself to the next level as a horseman/horsewoman or ride to improve your physical and mental health, we are committed to helping you Ride Onward TogetherĀ®. Join us as we explore the nuance of equine management and sports as well as interview industry professionals to provide you with the knowledge necessary to be a better partner for your equine friends.
I have uploaded two existing logos we use for various purposes to give you an idea of existing style.
Target Market(s)
Horse owners and other equine professionals
Look and feel
Each slider illustrates characteristics of the customer's brand and the style your logo design should communicate.

```html
<!DOCTYPE html>
<html lang="en">
<head>
<meta charset="utf-8">
<title>Ride Onward Together – Podcast Cover</title>
<link rel="stylesheet" href="https://fonts.googleapis.com/css2?family=Bebas+Neue&family=Oswald:wght@400;500&display=swap">
<style>
  :root {
    --paper: #e3e3de;
    --orange: #f04a00;
    --orange-deep: #d64400;
    --navy: #1f2f5c;
    --white: #ffffff;
    --photo-light: #9a9a98;
    --photo-mid: #5b5b5a;
    --photo-dark: #161616;
  }
  html, body {
    margin: 0;
    padding: 0;
    width: 1200px;
    height: 1200px;
    overflow: hidden;
    background: var(--paper);
  }
  .cover {
    position: relative;
    width: 1200px;
    height: 1200px;
    background: var(--paper);
    overflow: hidden;
  }
  .cover-art {
    position: absolute;
    inset: 0;
    width: 1200px;
    height: 1200px;
  }
  .brand-row {
    position: absolute;
    top: 70px;
    right: 36px;
    display: flex;
    align-items: center;
    gap: 36px;
  }
  .brand-name {
    font-family: "Oswald", sans-serif;
    font-weight: 500;
    color: var(--navy);
    font-size: 22px;
    letter-spacing: 1px;
    text-transform: uppercase;
    white-space: nowrap;
  }
  .brand-divider {
    width: 4px;
    height: 48px;
    background: var(--navy);
  }
  .partner {
    display: flex;
    align-items: center;
    gap: 10px;
  }
  .partner-dot {
    width: 22px;
    height: 22px;
    border-radius: 50%;
    background: var(--navy);
  }
  .partner .brand-name { font-size: 20px; }
  .title-line {
    position: absolute;
    left: 58px;
    margin: 0;
    background: var(--orange);
    color: var(--white);
    font-family: "Bebas Neue", sans-serif;
    font-weight: 400;
    font-size: 176px;
    line-height: 1;
    padding: 0 18px 0 20px;
    height: 156px;
    display: flex;
    align-items: center;
    letter-spacing: 1px;
    white-space: nowrap;
  }
  .title-line.first { top: 642px; }
  .title-line.second { top: 814px; height: 160px; }
  .tagline {
    position: absolute;
    left: 58px;
    top: 981px;
    width: 743px;
    height: 50px;
    box-sizing: border-box;
    background: var(--paper);
    color: var(--orange);
    font-family: "Oswald", sans-serif;
    font-weight: 400;
    font-size: 27px;
    line-height: 50px;
    padding-left: 14px;
    margin: 0;
    white-space: nowrap;
    transform: scaleX(0.82);
    transform-origin: left center;
  }
</style>
</head>
<body>
<main class="cover">
  <svg class="cover-art" viewBox="0 0 1200 1200" xmlns="http://www.w3.org/2000/svg">
    <defs>
      <linearGradient id="photoTone" x1="0" y1="0" x2="1" y2="1">
        <stop offset="0" stop-color="#6e6e6c"/>
        <stop offset="0.45" stop-color="#8c8c8a"/>
        <stop offset="0.8" stop-color="#3a3a39"/>
        <stop offset="1" stop-color="#0e0e0e"/>
      </linearGradient>
    </defs>
    <rect class="accent-block" x="851" y="392" width="208" height="730" fill="var(--orange-deep)"/>
    <polygon class="horse-photo" role="img" aria-label="Black and white close-up photo of a horse's head wearing a bridle"
      points="0,230 160,0 705,0 850,385 990,620 1145,980 1155,1130 1200,1200 0,1200"
      fill="url(#photoTone)"/>
    <rect class="accent-band top" x="0" y="187" width="583" height="84" fill="var(--orange)" opacity="0.85"/>
    <rect class="accent-band bottom" x="571" y="1122" width="629" height="78" fill="var(--orange-deep)" opacity="0.8"/>
  </svg>

  <div class="brand-row">
    <span class="brand-name">Ride Onward Together®</span>
    <span class="brand-divider"></span>
    <span class="partner">
      <span class="partner-dot"></span>
      <span class="brand-name">Still Meadow Farm</span>
    </span>
  </div>

  <h1 class="title-line first">Ride Onward</h1>
  <h1 class="title-line second">Together</h1>
  <p class="tagline">Join us as we Explore the Nuance of Equine Management and Sports</p>
</main>
</body>
</html>
```